Business Card Needed - Web Design (Promo Card)

Our web design company is currently offering a promo for new web sites.
$195 Setup
$95/mo
Month to Month, No Cancellation Fees
This is for a full web design for any company. We're looking to create promotional cards the size of business cards to promote this offer.
The cards should be very eye catching, could be cartoony, I really am open to any type of design. Our current business cards feature all our products and though very professional they are to detailed.
Here is our logo (doesn't necessary have to be included):
http://www.quorvelweb.com/images/lg-logo.png
Here are some card ideas I like.

```html
<!DOCTYPE html>
<html lang="en">
<head>
<meta charset="utf-8">
<title>Quorvel Web – Promo Card</title>
<link rel="stylesheet" href="https://fonts.googleapis.com/css2?family=Oswald:wght@300;400;500&family=Open+Sans:wght@400;700&display=swap">
<style>
  :root {
    --brand-blue: #2a6df4;
    --deep-blue: #1f5fe0;
    --accent-orange: #f07d1a;
    --ink: #1d1d1f;
    --card: #ffffff;
    --stage: #eef3fb;
    --edge: #1a1a1a;
  }
  * { margin: 0; padding: 0; box-sizing: border-box; }
  html, body {
    width: 1200px; height: 857px; overflow: hidden;
    background: var(--stage);
  }
  .canvas { position: relative; width: 1200px; height: 857px; }

  .card {
    position: absolute;
    width: 560px; height: 320px;
    background: var(--card);
    border: 2px solid var(--edge);
  }
  .card--front { left: 80px; top: 70px; }
  .card--back { left: 560px; top: 460px; }

  /* Front */
  .brand {
    position: absolute; left: 0; right: 0; top: 110px;
    display: flex; align-items: center; justify-content: center; gap: 18px;
  }
  .brand__dot {
    width: 64px; height: 64px; border-radius: 50%;
    background: var(--brand-blue);
  }
  .brand__name {
    font-family: "Open Sans", sans-serif; font-weight: 700;
    font-size: 56px; line-height: 1; color: var(--brand-blue);
    letter-spacing: -1px;
  }
  .tagline {
    position: absolute; left: 0; right: 0; top: 196px; text-align: center;
    font-family: "Open Sans", sans-serif; font-weight: 400;
    font-size: 20px; color: var(--brand-blue); letter-spacing: 1px;
  }

  /* Back */
  .offer {
    position: absolute; left: 0; top: 116px;
    width: 280px; height: 88px;
    background: var(--deep-blue); color: #fff;
    padding: 10px 0 0 40px;
    font-family: "Oswald", sans-serif;
  }
  .offer__price { font-size: 20px; font-weight: 500; line-height: 26px; }
  .offer__terms { font-size: 13px; font-weight: 300; line-height: 20px; }

  .contact {
    position: absolute; left: 300px; top: 88px;
    font-family: "Oswald", sans-serif; font-weight: 300;
    color: var(--ink);
  }
  .contact__address { font-size: 15px; margin-bottom: 18px; }
  .contact__list { display: grid; grid-template-columns: 58px 12px auto; row-gap: 2px; font-size: 14px; line-height: 20px; }
  .contact__label { color: var(--brand-blue); font-weight: 500; }
</style>
</head>
<body>
<main class="canvas">
  <section class="card card--front" aria-label="Card front">
    <div class="brand">
      <span class="brand__dot" aria-hidden="true"></span>
      <span class="brand__name">Quorvel Web</span>
    </div>
    <p class="tagline">Innovative Design &amp; Marketing</p>
  </section>

  <section class="card card--back" aria-label="Card back">
    <div class="offer">
      <p class="offer__price">$195 Setup</p>
      <p class="offer__price">$95/mo</p>
      <p class="offer__terms">Month to Month, No Cancellation Fees</p>
    </div>
    <div class="contact">
      <p class="contact__address">48 Harbor Lane, Milford Glen, CT 06519</p>
      <div class="contact__list">
        <span class="contact__label">Toll Free</span><span>:</span><span>888-555-0142</span>
        <span class="contact__label">Fax</span><span>:</span><span>203-555-0187</span>
        <span class="contact__label">Sales</span><span>:</span><span>sales@quorvelweb.com</span>
        <span class="contact__label">Support</span><span>:</span><span>support@quorvelweb.com</span>
        <span class="contact__label">Web</span><span>:</span><span>www.quorvelweb.com</span>
      </div>
    </div>
  </section>
</main>
</body>
</html>
```